Dental Business Card Design

Need to have a business card designed around my logo. I would like to have a unique, professional, and, eye catching designs. Can be associated with the colors within the logo, but not required and would actually like to see other color combinations that may work well with the logo. The back of the card is going to be an appointment reminder. I can provide you with the specific information for that needs to be on the back of the card if it's important for the design. i am an Oral Surgeon and the Business name is "Cedar Hollow Oral Surgery" The logo does have the name already incorporated into the design, however, if changing the fonts I would like to have the "Oral Surgery" emphasized. Please feel free to contact me with any questions as this is very important. I don't want to have any typical dental "tooth, mirror, etc." on the business card. Thank you.

```html
<!DOCTYPE html>
<html lang="en">
<head>
<meta charset="utf-8">
<title>Cedar Hollow Oral Surgery – Business Card</title>
<link href="https://fonts.googleapis.com/css2?family=Arimo:ital,wght@0,400;0,700;1,400;1,700&display=swap" rel="stylesheet">
<style>
  :root {
    --brand-blue: #136f9c;
    --brand-brown: #5b4235;
    --paper: #ffffff;
    --edge: #1a1a1a;
  }
  * { margin: 0; padding: 0; box-sizing: border-box; }
  html, body { width: 1200px; height: 900px; overflow: hidden; background: var(--paper); }
  body { position: relative; font-family: "Arimo", Arial, sans-serif; }

  /* Front of card */
  .card-front {
    position: absolute; left: 15px; top: 13px; width: 753px; height: 431px;
    border: 2px solid var(--edge); background: var(--paper); overflow: hidden;
  }
  .brand-mark {
    position: absolute; left: 168px; top: 40px; width: 100px; height: 100px;
    background: var(--brand-blue);
  }
  .brand-name {
    position: absolute; left: 0; top: 158px; width: 445px; text-align: center;
    color: var(--brand-blue); font-weight: 400; font-size: 40px; line-height: 42px;
    letter-spacing: 0.5px;
  }
  .doctor {
    position: absolute; left: 405px; top: 64px; color: var(--brand-brown);
    font-size: 15px; line-height: 19px;
  }
  .doctor-name {
    color: var(--brand-blue); font-weight: 700; font-size: 20px; line-height: 24px;
    margin-bottom: 4px;
  }
  .doctor-credential em { font-style: italic; }
  .contact-band {
    position: absolute; left: 0; top: 272px; width: 100%; height: 159px;
    background: var(--brand-blue); border-top: 3px solid var(--paper);
    box-shadow: 0 -2px 0 var(--brand-brown);
  }
  .contact {
    position: absolute; left: 65px; top: 27px; color: var(--paper);
    font-size: 18px; line-height: 30px;
  }
  .contact b { font-weight: 700; }
  .contact .sep { margin: 0 8px; }
  .contact .web { font-weight: 700; font-style: italic; }

  /* Back of card */
  .card-back {
    position: absolute; left: 430px; top: 452px; width: 754px; height: 431px;
    background: var(--brand-blue); border: 2px solid #0f4f70;
  }
  .frame-rim { position: absolute; inset: 14px; border: 4px solid var(--paper); }
  .frame-line { position: absolute; inset: 18px; border: 3px solid var(--brand-brown); }
  .frame-gap { position: absolute; inset: 21px; border: 5px solid var(--paper); }
  .reminder {
    position: absolute; inset: 36px; background: var(--paper);
    text-align: center; color: var(--brand-brown);
  }
  .next-line {
    margin-top: 38px; font-size: 21px; font-weight: 700; color: var(--brand-blue);
  }
  .days { margin-top: 14px; font-size: 18px; }
  .days .sep { margin: 0 7px; }
  .date-line { margin-top: 13px; font-size: 20px; font-weight: 700; color: var(--brand-blue); }
  .notes { margin-top: 52px; font-size: 15px; line-height: 20px; }
  .notes .label { font-weight: 700; font-style: italic; color: var(--brand-blue); }
  .notes .online { font-style: italic; color: var(--brand-blue); font-size: 16px; }
  .policy { margin-top: 32px; font-size: 16.5px; line-height: 21px; }
  .policy em { font-style: italic; }
  .policy b { color: var(--brand-blue); font-weight: 700; }
</style>
</head>
<body>

<section class="card-front">
  <div class="brand-mark"></div>
  <div class="brand-name">Cedar Hollow<br>Oral Surgery</div>

  <div class="doctor">
    <div class="doctor-name">Daniel R. Whitford DDS, MD</div>
    <div class="doctor-credential">Diplomate, <em>Midland Council of Oral<br>&amp; Maxillofacial Surgeons</em></div>
  </div>

  <div class="contact-band">
    <div class="contact">
      <div>2210 Alder Lane<span class="sep">|</span>Lincoln, NE 68510</div>
      <div><b>Phone:</b> (555) 214-3380<span class="sep">|</span><b>Fax:</b> (555) 214-3381</div>
      <div class="web">www.cedarhollowos.com</div>
    </div>
  </div>
</section>

<section class="card-back">
  <div class="frame-rim"></div>
  <div class="frame-line"></div>
  <div class="frame-gap"></div>
  <div class="reminder">
    <p class="next-line">Your next appointment is for: _______________on: _________</p>
    <p class="days">Monday<span class="sep">|</span>Tuesday<span class="sep">|</span>Wednesday<span class="sep">|</span>Thursday<span class="sep">|</span>Friday<span class="sep">|</span>Saturday</p>
    <p class="date-line">Date: __________ Time:__________</p>
    <p class="notes">
      <span class="label">Please remember:</span> Nothing to eat or drink 6 hours prior to IV Sedation.<br>
      Bring any necessary x-rays, medications, and referral slips.<br>
      <span class="online">Save time by filling out your Medical history online</span>
    </p>
    <p class="policy">
      <em>A broken appointment is a loss for everyone.</em> <b>Please inform us 24 hours<br>
      in advance if you are unable to keep your appointment or you may be<br>
      charged for a missed visit.</b>
    </p>
  </div>
</section>

</body>
</html>
```